Long Established Local Fencing (not swords) Business needs fresh Business Cards

We need fresh double sided business cards for our Fencing Construction business, we are looking for something with our new logo design added, and maybe a photo background ?
We recently had cards made from Quillmarko and we were horrified with what we got back, the quality was terrible, so am looking for high quality format for good printing company to make.
We install Steelwave, Timber paling, Aluminium Slat Screening, Picket (timber and aluminium) and most other fencing installations.
Our website is brelbanfencing.com.au should you like to learn a bit more.
We do have logo in other formats if required.
We have been in business for over 35 years and we have used this as a "motto" it is on our signage

Industry/Entity Type

Construction

Contact Information for Business Card

Open to ideas, we need 3 x different cards, one generic with no name and 2 x others each with 1 of our bosses name on each, I will put into upload files.

Colors
ec1f27
000000
606060
f5f5f5

Requirements
Must have
• Company Name and Logo
• Address
• Contact details, phone, website, email etc
• Small space to write notes when leaving card at residence
Nice to have
• Our motto "Servicing the Peninsula for over 35 years"

```html
<!DOCTYPE html>
<html lang="en">
<head>
<meta charset="utf-8">
<title>Brelban Fencing – Business Cards</title>
<link rel="stylesheet" href="https://fonts.googleapis.com/css2?family=Lato:wght@400;700;900&display=swap">
<style>
  :root {
    --red: #ec1f27;
    --black: #111213;
    --grey: #606060;
    --light: #f5f5f5;
    --back-card: #e4e4e4;
    --stage: #2b2b2c;
    --white: #ffffff;
  }
  * { margin: 0; padding: 0; box-sizing: border-box; }
  html, body {
    width: 1200px; height: 782px; overflow: hidden;
    background: var(--stage);
    font-family: "Lato", sans-serif;
  }
  .canvas { position: relative; width: 1200px; height: 782px; }

  .card {
    position: absolute;
    width: 525px; height: 300px;
    overflow: hidden;
    box-shadow: 0 12px 30px rgba(0,0,0,.45);
  }

  /* Back side – notes */
  .card-back { left: 610px; top: 110px; background: var(--back-card); }
  .card-back .faint-name {
    position: absolute; left: 0; right: 0; top: 100px;
    text-align: center; font-weight: 900; font-size: 40px;
    color: rgba(96,96,96,.10); letter-spacing: 1px;
  }
  .note-line {
    position: absolute; left: 70px; right: 40px;
    height: 1px; background: var(--grey);
  }
  .note-line:nth-of-type(1) { top: 60px; }
  .note-line:nth-of-type(2) { top: 105px; }
  .note-line:nth-of-type(3) { top: 150px; }
  .note-line:nth-of-type(4) { top: 195px; }
  .motto {
    position: absolute; left: 70px; bottom: 42px;
    color: var(--red); font-weight: 700; font-size: 16px;
    text-transform: uppercase; letter-spacing: .6px;
  }

  /* Front side */
  .card-front { left: 70px; top: 380px; background: var(--white); }
  .swoosh { position: absolute; inset: 0; }
  .person { position: absolute; left: 30px; top: 30px; }
  .person-name { font-weight: 900; font-size: 19px; letter-spacing: .5px; text-transform: uppercase; }
  .person-name .first { color: var(--red); }
  .person-name .last { color: var(--grey); }
  .person-role { font-size: 12px; color: #333; margin-top: 2px; }

  .contact { position: absolute; left: 30px; top: 118px; list-style: none; }
  .contact li { display: flex; align-items: center; gap: 6px; font-size: 14px; color: #222; margin-bottom: 5px; }
  .contact svg { width: 15px; height: 15px; flex: none; }

  .brand {
    position: absolute; right: 40px; top: 122px;
    display: flex; align-items: center; gap: 10px;
  }
  .brand-dot { width: 18px; height: 18px; border-radius: 50%; background: var(--red); }
  .brand-name {
    font-weight: 900; font-size: 30px; line-height: 1.02;
    color: var(--black); text-transform: uppercase; letter-spacing: .5px;
  }

  .website {
    position: absolute; right: 40px; bottom: 10px;
    color: var(--white); font-size: 14px; letter-spacing: .4px;
  }
</style>
</head>
<body>
<main class="canvas">

  <section class="card card-back" aria-label="Card back with space for notes">
    <div class="faint-name" aria-hidden="true">BRELBAN FENCING</div>
    <span class="note-line"></span>
    <span class="note-line"></span>
    <span class="note-line"></span>
    <span class="note-line"></span>
    <p class="motto">Servicing the Peninsula for over 35 years</p>
  </section>

  <section class="card card-front" aria-label="Card front">
    <svg class="swoosh" viewBox="0 0 525 300" preserveAspectRatio="none" aria-hidden="true">
      <path d="M0,205 C100,212 170,258 270,266 C370,272 450,262 525,250 L525,300 L0,300 Z" fill="var(--black)"/>
      <path d="M0,182 C80,182 150,205 245,252 C160,222 80,199 0,194 Z" fill="var(--grey)"/>
      <path d="M270,256 C370,252 450,232 525,208 L525,238 C450,254 370,262 270,256 Z" fill="var(--red)"/>
    </svg>

    <div class="person">
      <p class="person-name"><span class="first">Marcus</span> <span class="last">Hale</span></p>
      <p class="person-role">Managing Director</p>
    </div>

    <ul class="contact">
      <li>
        <svg viewBox="0 0 16 16" aria-hidden="true"><circle cx="8" cy="8" r="8" fill="var(--red)"/><path d="M5.5 4.5l1.3 0 .6 1.8-.9.7c.4.9 1 1.5 1.9 1.9l.7-.9 1.8.6v1.3c0 .5-.4.8-.9.8-2.8-.2-5-2.4-5.2-5.2 0-.5.3-1 .7-1z" fill="var(--white)"/></svg>
        444 555 6688
      </li>
      <li>
        <svg viewBox="0 0 16 16" aria-hidden="true"><circle cx="8" cy="8" r="8" fill="var(--red)"/><rect x="4" y="5" width="8" height="6" rx="1" fill="var(--white)"/><path d="M4.3 5.4L8 8.3l3.7-2.9" stroke="var(--red)" stroke-width="1" fill="none"/></svg>
        info@youremail.com
      </li>
    </ul>

    <div class="brand">
      <span class="brand-dot" aria-hidden="true"></span>
      <span class="brand-name">Brelban<br>Fencing</span>
    </div>

    <p class="website">www.websitename.com</p>
  </section>

</main>
</body>
</html>
```